Billboard advertisement design

Health & Fitness centre requires a billboard advertisement design for an allocated space out the front of the shopping centre in which it is located. Kestrel Ridge Health & Fitness is located in a small town with one other competitor. Looking for a fun, trendy sign to draw people's attention and make sure Kestrel Ridge is instantly recognisable. Sign location is in the middle of town on the national highway. Approximate size is 12' x 5'. Final design will encourage people who have been thinking about joining the gym to take the first step in leading a fitter and healthier lifestyle.

Target Market(s)

Health conscious members of the community that have been thinking about taking the next step and joining a gym

Industry/Entity Type

Shopping

Requirements
Must have
• Please utilise attached logo
Nice to have
• Contact info is (07) 4918 5307 info@kestrelridgefitness.example.com.au

```html
<!DOCTYPE html>
<html lang="en">
<head>
<meta charset="utf-8">
<title>Kestrel Ridge Health &amp; Fitness — Billboard</title>
<link rel="stylesheet" href="https://fonts.googleapis.com/css2?family=Questrial&display=swap">
<style>
  :root {
    --stage: #e6e8eb;
    --orange: #f47b20;
    --orange-light: #fbd9bd;
    --cream: #fff7f0;
    --brand-blue: #1d4f9c;
    --icon-orange: #e8561c;
    --rule: #e9a878;
    --arm-brown: #4b1c0a;
    --weight-dark: #2b2b2b;
  }
  * { margin: 0; padding: 0; box-sizing: border-box; }
  html, body {
    width: 1200px;
    height: 900px;
    overflow: hidden;
    background: var(--stage);
  }
  .billboard {
    position: absolute;
    left: 50px;
    top: 220px;
    width: 1100px;
    height: 459px;
    overflow: hidden;
    background: linear-gradient(180deg, var(--cream) 0%, var(--orange-light) 30%, var(--orange) 75%, var(--orange) 100%);
    box-shadow: 0 6px 18px rgba(0, 0, 0, 0.25);
    font-family: "Questrial", "Century Gothic", sans-serif;
  }
  .billboard__arm {
    position: absolute;
    left: 0;
    top: 30px;
    width: 306px;
    height: 429px;
    background: var(--arm-brown);
    border-radius: 0 120px 40px 0;
  }
  .billboard__dumbbell {
    position: absolute;
    left: 335px;
    top: 258px;
    width: 288px;
    height: 158px;
    background: linear-gradient(180deg, #444 0%, var(--weight-dark) 100%);
    border-radius: 60px;
  }
  .contact {
    position: absolute;
    left: 640px;
    top: 38px;
    width: 402px;
    color: var(--brand-blue);
  }
  .contact__brand {
    font-size: 44px;
    line-height: 1;
    letter-spacing: 0.5px;
    white-space: nowrap;
  }
  .contact__brand-sub {
    display: block;
    font-size: 14px;
    letter-spacing: 26px;
    margin-top: 4px;
  }
  .contact__rule {
    height: 2px;
    background: var(--rule);
    margin: 8px 0 14px;
  }
  .contact__line {
    display: flex;
    align-items: center;
    gap: 10px;
    white-space: nowrap;
  }
  .contact__email {
    font-size: 21px;
  }
  .contact__phone {
    font-size: 42px;
    letter-spacing: 2px;
    margin-top: 26px;
  }
  .contact__icon { flex: none; fill: var(--icon-orange); }
</style>
</head>
<body>
  <main class="billboard">
    <div class="billboard__arm" role="img" aria-label="Illustration of a flexed muscular arm"></div>
    <div class="billboard__dumbbell" role="img" aria-label="Illustration of a black dumbbell"></div>

    <section class="contact">
      <h1 class="contact__brand">KESTREL RIDGE<span class="contact__brand-sub">FITNESS</span></h1>
      <div class="contact__rule"></div>
      <p class="contact__line contact__email">
        <svg class="contact__icon" width="24" height="16" viewBox="0 0 24 16" aria-hidden="true">
          <rect x="0" y="0" width="24" height="16" rx="1"/>
          <path d="M1 1 L12 9 L23 1" fill="none" stroke="#fff" stroke-width="1.6"/>
        </svg>
        info@kestrelridgefitness.example.com.au
      </p>
      <p class="contact__line contact__phone">
        <svg class="contact__icon" width="26" height="42" viewBox="0 0 26 42" aria-hidden="true">
          <path d="M9 2 C4 3 1 8 1 16 C1 26 6 36 12 40 C14 41 17 40 19 38 L21 35 C22 33 21 32 20 31 L15 27 C14 26 12 26 11 28 L10 29 C7 25 6 19 6 15 L8 14 C10 13 10 12 10 10 L9 4 C9 2 9 2 9 2 Z"/>
        </svg>
        (07) 4918 5307
      </p>
    </section>
  </main>
</body>
</html>
```